Bluefinch Painting needs a Website

We need a website built for a Painting company I own, we mainly do residential painting, but don't want to be limited to that.

Need to have estimate request form.
Need pic's of past projects

I like the look of the website for http://www.harborline-painters.example
& "Thistledown Property inspections"

My logo that was designed here on ArtHive on the front page

I would like one of the houses I downloaded as part of the background
of the front page.

Target Market(s)

Home owners

Industry/Entity Type

Painting

Number of Pages Required

1 page

Font styles to use
Serif

Requirements
Must have
• Estimate request form for home owners to fill out -
• Name:
• Phone Number:
• Address:
• E-mail:
• Painting project description:
• And my info to:
• My phone number: (555) 318-7764
• My web address bluefinchpainting.example
Nice to have
• My logo that was designed here on ArtHive

```html
<!DOCTYPE html>
<html lang="en">
<head>
<meta charset="utf-8">
<title>Bluefinch Painting</title>
<link href="https://fonts.googleapis.com/css2?family=Noto+Serif:wght@400;700&family=Arimo:wght@400;700&display=swap" rel="stylesheet">
<style>
:root{
  --blue:#1b7fc8;
  --blue-dark:#1464a8;
  --black:#000;
  --footer:#111;
  --text:#333;
  --white:#fff;
  --line:#c9c9c9;
  --serif:"Noto Serif",serif;
  --sans:"Arimo",sans-serif;
}
*{margin:0;padding:0;box-sizing:border-box}
html,body{width:930px;height:1200px;overflow:hidden;background:var(--white)}
body{position:relative;font-family:var(--sans);color:var(--text)}
.abs{position:absolute}

/* header */
.brand{left:123px;top:14px;display:flex;align-items:center;gap:10px}
.brand-mark{width:40px;height:40px;background:var(--blue);border-radius:50%}
.brand-name{font-family:var(--serif);font-size:23px;color:var(--black);letter-spacing:1px;line-height:1}
.trailer{left:502px;top:8px;width:152px;height:70px;background:linear-gradient(#f2f2f2,#c9ccd0);border:1px solid #bbb}
.estimate-btn{left:680px;top:3px;width:116px;height:23px;background:var(--blue);color:var(--white);font-size:13px;text-align:center;line-height:23px}
.call{left:683px;top:38px;display:flex;align-items:center;gap:6px}
.call-label{font-size:10.5px;color:#222;line-height:1.2}
.call-number{font-size:15.5px;color:#222}

/* navigation */
.nav{left:0;top:78px;width:930px;height:31px;background:var(--blue);display:flex;padding-left:125px}
.nav a{font-family:var(--serif);font-size:11.5px;color:var(--white);text-decoration:none;height:31px;line-height:31px;text-align:center;border-right:1px solid rgba(255,255,255,.35)}
.nav a.active{background:var(--black);font-weight:700;border-right:none}

/* hero */
.hero{left:0;top:109px;width:930px;height:308px;background:linear-gradient(180deg,#3a55c4 0%,#3550b8 45%,#7b5a3a 80%,#3c3a3e 100%)}
.hero-title{left:520px;top:157px;width:248px;text-align:center;font-family:var(--serif);font-size:17.5px;line-height:24px;color:var(--white)}
.arrow-btn{width:26px;height:26px;background:rgba(255,255,255,.85);display:flex;align-items:center;justify-content:center}

/* welcome */
.welcome{left:0;top:417px;width:930px;height:167px;background:var(--blue);color:var(--white);text-align:center}
.welcome h1{position:absolute;top:20px;width:100%;font-family:var(--serif);font-weight:400;font-size:17px}
.welcome p{position:absolute;left:135px;top:67px;width:660px;font-size:9.6px;line-height:17px}
.read-more{background:var(--black);color:var(--white);font-size:10px;height:19px;line-height:19px;text-align:center;border-radius:2px}

/* columns */
.col-title{font-family:var(--serif);font-size:16.5px;color:#222;font-weight:400}
.photo{border:2px solid #ddd;box-shadow:0 0 0 1px #bbb}
.col-text{font-size:9.3px;line-height:14.5px;color:#333;width:210px}
.field{left:609px;width:198px;height:20px;border:1px solid #bbb;border-radius:3px;font-size:8.5px;font-style:italic;color:#666;padding:4px 8px}

/* gallery */
.thumb{top:932px;width:120px;height:96px;border:1px solid #555;padding:4px}
.thumb div{width:100%;height:100%}

/* footer */
.footer{left:0;top:1041px;width:930px;height:133px;background:var(--footer);color:var(--white)}
.footer h3{position:absolute;font-size:9.5px;font-weight:700;padding-bottom:3px;border-bottom:1px dashed #777}
.footer ul{list-style:none;font-size:9.3px;line-height:15.5px}
.footer .info{font-size:9.3px;line-height:13.5px}
.bottom-bar{left:0;top:1174px;width:930px;height:26px;background:var(--blue);color:var(--white);font-size:9px;text-align:center;line-height:26px}
.card{width:21px;height:14px;border-radius:2px}
</style>
</head>
<body>

<!-- header -->
<div class="abs brand"><span class="brand-mark"></span><span class="brand-name">BLUEFINCH PAINTING</span></div>
<div class="abs trailer" role="img" aria-label="Company work trailer with Bluefinch Painting signage"></div>
<div class="abs estimate-btn">Free Estimates</div>
<div class="abs call">
  <svg width="24" height="24" viewBox="0 0 24 24"><circle cx="12" cy="12" r="10.5" fill="none" stroke="#1b7fc8" stroke-width="1.5"/><path d="M9 6c-1 1-2 3 0 7s4 5 6 5l1-2-2-2-1 1c-1-.5-2-2-2.5-3l1-1-1-3z" fill="#1b7fc8"/></svg>
  <div><div class="call-label">Call Us Today</div><div class="call-number">555-318-7764</div></div>
</div>

<!-- navigation -->
<nav class="abs nav">
  <a class="active" style="width:56px">Home</a>
  <a style="width:91px">About Us</a>
  <a style="width:80px">Exterior</a>
  <a style="width:78px">Interior</a>
  <a style="width:96px">Residential</a>
  <a style="width:102px">Commerical</a>
  <a style="width:104px">Past Projects</a>
  <a style="width:106px;border-right:none">Contact Us</a>
</nav>

<!-- hero -->
<div class="abs hero" role="img" aria-label="Freshly painted office interior with blue walls and orange accents"></div>
<div class="abs hero-title">PROVIDING QUALITY<br>WORK AT<br>AFFORDABLE PRICES</div>
<div class="abs arrow-btn" style="left:5px;top:225px"><svg width="10" height="10" viewBox="0 0 10 10"><path d="M7 1L3 5l4 4" stroke="#333" stroke-width="2" fill="none"/></svg></div>
<div class="abs arrow-btn" style="left:896px;top:225px"><svg width="10" height="10" viewBox="0 0 10 10"><path d="M3 1l4 4-4 4" stroke="#333" stroke-width="2" fill="none"/></svg></div>

<!-- welcome -->
<section class="abs welcome">
  <h1>Welcome to Bluefinch Painting</h1>
  <svg class="abs" style="left:331px;top:46px" width="268" height="12" viewBox="0 0 268 12"><line x1="0" y1="3" x2="268" y2="3" stroke="#fff"/><line x1="0" y1="6" x2="268" y2="6" stroke="#fff"/><path d="M130 4l8 7M138 4l-8 7" stroke="#fff"/></svg>
  <p>Lorem ipsum dolor sit amet, consectetuer adipiscing elit, sed diam nonummy nibh euismod&nbsp; rent ut laoreet dolore magna aliquam erat volutpat. Ut wisi enim ad minim veniam, quis nostrud lore xererci tation ullamcorper suscipit lobortis nisl ut aliquip ex ea commodo consequat. Duis autem revel eum iriure dolor in hendrerit in vulputate velit esse molestie consequat.</p>
  <svg class="abs" style="left:369px;top:134px" width="192" height="8" viewBox="0 0 192 8"><line x1="0" y1="4" x2="192" y2="4" stroke="#fff"/><path d="M54 2h14M54 6h14M124 2h14M124 6h14" stroke="#fff"/></svg>
  <div class="abs read-more" style="left:435px;top:130px;width:60px">Read More</div>
</section>

<!-- services -->
<h2 class="abs col-title" style="left:133px;top:601px">Residential Painting</h2>
<div class="abs photo" style="left:133px;top:633px;width:207px;height:131px;background:linear-gradient(135deg,#8a7a68,#d8c9b0 55%,#5a4d40)" role="img" aria-label="Painted living room interior"></div>
<p class="abs col-text" style="left:134px;top:769px">Sed ut perspiciatis unde omnis iste natus error sit voluptatem accusantium doloremque laudantium, totam rem aperiam.</p>
<div class="abs read-more" style="left:134px;top:818px;width:60px">Read More</div>

<h2 class="abs col-title" style="left:370px;top:601px">Commerical Painting</h2>
<div class="abs photo" style="left:371px;top:633px;width:207px;height:131px;background:linear-gradient(135deg,#e4e2dc,#f4f2ec 60%,#c6bfae)" role="img" aria-label="Painter on a ladder rolling paint onto a wall"></div>
<p class="abs col-text" style="left:373px;top:769px">Sed ut perspiciatis unde omnis iste natus error sit voluptatem accusantium doloremque laudantium, totam rem aperiam.</p>
<div class="abs read-more" style="left:373px;top:818px;width:60px">Read More</div>

<!-- inquiry form -->
<h2 class="abs col-title" style="left:607px;top:601px">Quick Inquiry</h2>
<div class="abs" style="left:607px;top:626px;width:203px;border-top:1px dashed #aaa"></div>
<div class="abs field" style="top:637px">Name</div>
<div class="abs field" style="top:665px">Email</div>
<div class="abs field" style="top:694px">Phone</div>
<div class="abs field" style="top:722px">Type of Work</div>
<div class="abs field" style="top:752px;height:59px">Message</div>
<div class="abs read-more" style="left:613px;top:818px;width:61px;font-weight:700">Submit</div>

<!-- gallery -->
<div class="abs" style="left:133px;top:866px;width:672px;height:1px;background:linear-gradient(90deg,transparent,#ccc,transparent)"></div>
<svg class="abs" style="left:137px;top:885px" width="40" height="40" viewBox="0 0 40 40"><circle cx="20" cy="20" r="19" fill="#fff" stroke="#ccc"/><rect x="13" y="15" width="13" height="12" fill="none" stroke="#333" stroke-width="2"/><path d="M16 12h11v11" fill="none" stroke="#333" stroke-width="2"/></svg>
<h2 class="abs col-title" style="left:186px;top:894px">Our Work Gallery</h2>
<svg class="abs" style="left:770px;top:898px" width="31" height="15" viewBox="0 0 31 15"><rect width="14" height="15" fill="#111"/><path d="M9 3L5 7.5 9 12" stroke="#fff" stroke-width="2" fill="none"/><rect x="17" width="14" height="15" fill="#1b7fc8"/><path d="M22 3l4 4.5-4 4.5" stroke="#fff" stroke-width="2" fill="none"/></svg>
<div class="abs thumb" style="left:137px"><div role="img" aria-label="Entry hall with staircase and wood floor" style="background:linear-gradient(#d9c8a8,#8a4e2a)"></div></div>
<div class="abs thumb" style="left:271px"><div role="img" aria-label="Exterior siding being painted" style="background:linear-gradient(#2d64b4,#dfe4ea 40%,#cfd4dc)"></div></div>
<div class="abs thumb" style="left:405px"><div role="img" aria-label="Yellow painted hallway" style="background:linear-gradient(135deg,#e8c64a,#f0e2b0 60%,#b07040)"></div></div>
<div class="abs thumb" style="left:539px"><div role="img" aria-label="Freshly painted house exterior" style="background:linear-gradient(#cfe0ee,#c8b8a0 50%,#5a9a3a)"></div></div>
<div class="abs thumb" style="left:672px"><div role="img" aria-label="White staircase in bright foyer" style="background:linear-gradient(135deg,#f2ecd8,#d8b878)"></div></div>

<!-- footer -->
<footer class="abs footer">
  <h3 style="left:133px;top:16px;width:74px">Quick Links</h3>
  <ul class="abs" style="left:133px;top:38px">
    <li>• Home</li><li>• About Us</li><li>• Services</li><li>• Past Projects</li><li>• Contact Us</li>
  </ul>
  <h3 style="left:290px;top:16px;width:116px">Contact Information</h3>
  <div class="abs info" style="left:291px;top:37px"><b>A:</b></div>
  <div class="abs info" style="left:313px;top:36px">Bluefinch Painting<br>Street Name City Name<br>State Zipcode</div>
  <div class="abs info" style="left:291px;top:85px"><b>P:</b></div>
  <div class="abs info" style="left:313px;top:85px">555-318-7764</div>
  <div class="abs info" style="left:291px;top:104px"><b>E:</b></div>
  <div class="abs info" style="left:313px;top:103px">inquiry@bluefinchp.example</div>

  <h3 style="left:472px;top:16px;width:111px">Work Times</h3>
  <svg class="abs" style="left:474px;top:40px" width="11" height="10" viewBox="0 0 11 10"><path d="M1 4h9v5H1z M3 4V2h5v2" fill="none" stroke="#fff"/></svg>
  <div class="abs info" style="left:489px;top:38px;font-size:8.8px">Our work timings are:</div>
  <svg class="abs" style="left:474px;top:62px" width="11" height="11" viewBox="0 0 11 11"><circle cx="5.5" cy="5.5" r="4.5" fill="none" stroke="#fff"/><path d="M5.5 3v3h2" fill="none" stroke="#fff"/></svg>
  <div class="abs info" style="left:489px;top:60px;font-size:8.8px">Monday - Friday. 8AM - 8PM</div>
  <svg class="abs" style="left:474px;top:85px" width="11" height="11" viewBox="0 0 11 11"><circle cx="5.5" cy="5.5" r="4.5" fill="none" stroke="#fff"/><path d="M5.5 3v3h2" fill="none" stroke="#fff"/></svg>
  <div class="abs info" style="left:489px;top:83px;font-size:8.8px">Saturday:9AM - 4PM</div>
  <svg class="abs" style="left:474px;top:106px" width="11" height="11" viewBox="0 0 11 11"><circle cx="5.5" cy="5.5" r="4.5" fill="none" stroke="#fff"/><path d="M3.5 7.5h4" stroke="#fff"/></svg>
  <div class="abs info" style="left:489px;top:104px;font-size:8.8px">Sunday: closed</div>

  <div class="abs" style="left:660px;top:28px;display:flex;align-items:center;gap:6px"><span style="width:16px;height:16px;background:#fff;border-radius:50%"></span><span style="font-family:var(--serif);font-size:12px;letter-spacing:.5px">BLUEFINCH PAINTING</span></div>
  <div class="abs" style="left:658px;top:63px;width:146px;text-align:center;font-size:9.5px">We Accept</div>
  <div class="abs" style="left:673px;top:80px;display:flex;gap:3px">
    <span class="card" style="background:#2a66c8"></span>
    <span class="card" style="background:#e8e8e8"></span>
    <span class="card" style="background:#1d3f9a"></span>
    <span class="card" style="background:#3aa0d8"></span>
    <span class="card" style="background:#e8551e"></span>
  </div>
</footer>
<div class="abs bottom-bar">Copyright ©2015, BluefinchPainting&nbsp; All Rights Reserved</div>

</body>
</html>
```